Upmarket building and construction company needs signage

Our building company R Brent Construction, needs signage to put up on the side of our vehicle trailers and on site fencing. We are a building company that specialises in residential construction and carpentry .

I will attach our logo and some inspirational pics for site fencing as well as what our trailer looks like .
Other details i would like on the sign are our
( email) rbrentconstruction@mailbox-example.net
(mobile ) 0493 518 264
(website ) rbrentconstruction. example.net

Target Market(s)

Home owners looking for a reliable local builder who produces good quality work. I have attached some inspirational pics.

Industry/Entity Type

Building and Construction

Colors

Designer to choose colors to be used in the design.

Requirements
Must have
• Our logo, contact information
Nice to have
• We would like the design to have elements of being Elegant, Serious, Modern, Professional, Masculine, Conservative and Upmarket.

```html
<!DOCTYPE html>
<html lang="en">
<head>
<meta charset="utf-8">
<title>R Brent Construction – Trailer Signage</title>
<link rel="stylesheet" href="https://fonts.googleapis.com/css2?family=Jost:wght@400;700&display=swap">
<style>
  :root {
    --brand-orange: #c96c1a;
    --brand-grey: #747474;
    --ink-grey: #707070;
    --frame-grey: #7a7a7a;
    --paper: #ffffff;
  }
  * { box-sizing: border-box; margin: 0; padding: 0; }
  html, body {
    width: 1200px; height: 517px; overflow: hidden;
    background: var(--paper);
    font-family: "Jost", "Futura", sans-serif;
  }
  .canvas { position: relative; width: 1200px; height: 517px; }

  .sign-title {
    position: absolute; top: 92px;
    font-size: 23px; font-weight: 400; color: var(--ink-grey);
    transform: translateX(-50%); white-space: nowrap;
  }
  .sign-title--side { left: 376px; }
  .sign-title--front { left: 946px; }

  .sign {
    position: absolute; top: 165px; height: 228px;
    border: 1px solid var(--frame-grey); background: var(--paper); overflow: hidden;
  }
  .sign--side { left: 92px; width: 569px; }
  .sign--front { left: 775px; width: 342px; }

  .wordmark {
    position: absolute; color: var(--ink-grey); font-weight: 400;
    text-transform: uppercase; line-height: 1.1; white-space: nowrap;
  }
  .sign--side .wordmark {
    left: 32px; top: 100px; width: 210px;
    font-size: 23px; letter-spacing: 1px;
  }
  .sign--front .wordmark {
    left: 0; right: 0; top: 76px; text-align: center;
    font-size: 19px; letter-spacing: 1px;
  }
  .wordmark__mark {
    display: inline-block; width: 0.45em; height: 0.45em;
    background: var(--brand-orange); margin-right: 0.3em; vertical-align: 0.1em;
  }

  /* Side trailer panels */
  .side-phone-panel {
    position: absolute; left: 265px; top: 0; width: 304px; height: 151px;
    background: var(--brand-orange);
  }
  .side-contact-panel {
    position: absolute; left: 265px; top: 158px; width: 280px; height: 70px;
    background: var(--brand-grey);
  }
  .side-contact-tail {
    position: absolute; left: 550px; top: 158px; width: 19px; height: 70px;
    background: var(--brand-grey);
  }
  .phone {
    color: var(--paper); font-weight: 700; white-space: nowrap; letter-spacing: 0.5px;
  }
  .side-phone-panel .phone {
    position: absolute; left: 34px; top: 22px; font-size: 23px;
  }
  .contact-lines { color: var(--paper); white-space: nowrap; line-height: 1.3; }
  .side-contact-panel .contact-lines {
    position: absolute; left: 26px; top: 16px; font-size: 13px;
  }

  /* Front trailer panels */
  .front-phone-panel {
    position: absolute; left: 0; bottom: 0; width: 170px; height: 54px;
    background: var(--brand-orange);
    display: flex; align-items: center; justify-content: center;
  }
  .front-phone-panel .phone { font-size: 20px; }
  .front-contact-panel {
    position: absolute; right: 0; bottom: 0; width: 170px; height: 54px;
    background: var(--brand-grey);
    display: flex; align-items: center; justify-content: center;
  }
  .front-contact-panel .contact-lines { font-size: 8.6px; text-align: center; }
</style>
</head>
<body>
<main class="canvas">
  <h2 class="sign-title sign-title--side">Side Trailer</h2>
  <h2 class="sign-title sign-title--front">Front Trailer</h2>

  <section class="sign sign--side" aria-label="Side trailer sign">
    <p class="wordmark"><span class="wordmark__mark"></span>R Brent<br>Construction</p>
    <div class="side-phone-panel">
      <p class="phone">0493 518 264</p>
    </div>
    <div class="side-contact-panel">
      <p class="contact-lines">rbrentconstruction@mailbox-example.net<br>rbrentconstruction.example.net</p>
    </div>
    <div class="side-contact-tail"></div>
  </section>

  <section class="sign sign--front" aria-label="Front trailer sign">
    <p class="wordmark"><span class="wordmark__mark"></span>R Brent<br>Construction</p>
    <div class="front-phone-panel">
      <p class="phone">0493 518 264</p>
    </div>
    <div class="front-contact-panel">
      <p class="contact-lines">rbrentconstruction@mailbox-example.net<br>rbrentconstruction.example.net</p>
    </div>
  </section>
</main>
</body>
</html>
```